Holt & Partners Property Management

I want 4 different cards so that i can mail to my farm once per quarter. I want to go back to a 5X8 card or smaller. I am attaching an example of what we did in the past. I would like the new cards start with the following:
1. Tired of dealing with tenant problems at 6:00 on a Friday Night?
2. Would you like to take you next vacation worry free?
3. Are your tenants paying below market rents?
4. Do your tenant leases fully protect you?
I would like to have one of these "hooks" to lead off each card with a brief explanation of the services we provide. Back of the card can be similar to the one I attached.

Target Market(s)

Income Property Owners that might be in need of a property management company.

Font styles to use
Serif

Requirements
Must have
• 4 separate cards that i can email out each quarter.
• Each card must have a "hook" or "call to action"
Nice to have
• Less verbiage and some catchy graphics or photo
• If you have an idea for catchier calls to action, feel free to submit.
Should not have
• Too many words. The postcard I uploaded has way too much verbiage.

```html
<!DOCTYPE html>
<html lang="en">
<head>
<meta charset="utf-8">
<title>Holt &amp; Partners Property Management – Quarterly Postcards</title>
<link rel="stylesheet" href="https://fonts.googleapis.com/css2?family=Open+Sans:ital,wght@0,400;0,600;0,700;0,800;1,700&family=Oswald:wght@500&display=swap">
<style>
  :root{
    --tan:#b69a63;
    --tan-light:#c8ae78;
    --charcoal:#4a4a4a;
    --charcoal-dark:#3c3c3c;
    --silver:#e4e4e4;
    --silver-dark:#c9c9c9;
    --white:#ffffff;
    --ink:#3a3a3a;
    --page:#ece9e4;
  }
  *{box-sizing:border-box;margin:0;padding:0}
  html,body{width:910px;height:1200px;overflow:hidden;background:var(--page)}
  body{font-family:"Open Sans",Arial,sans-serif;position:relative}

  .card{position:absolute;width:366px;height:230px;background:var(--white);overflow:hidden;
        box-shadow:0 6px 12px rgba(0,0,0,.28)}
  .card .shapes{position:absolute;inset:0;width:366px;height:230px}
  .col-front{left:68px}
  .col-back{left:476px}
  .row-1{top:38px}.row-2{top:337px}.row-3{top:634px}.row-4{top:932px}

  /* front */
  .photo{position:absolute;left:170px;top:0;width:196px;height:230px;
         background:linear-gradient(180deg,#8fb4d8 0%,#cfd9e0 28%,#e6e0d2 45%,#b8a68a 62%,#3b3633 80%,#262424 100%)}
  .brand{position:absolute;left:12px;top:10px;color:var(--white);font-weight:400;line-height:1}
  .brand .name{font-size:14px;letter-spacing:.3px;display:block;line-height:14px}
  .brand .sub{font-size:7px;display:block;margin-top:8px;letter-spacing:.2px}
  .broker{position:absolute;left:163px;top:7px;font-size:7.5px;font-weight:700;color:var(--white)}
  .broker .label{color:var(--tan-light)}
  .hotline{position:absolute;left:146px;top:33px;display:flex;align-items:center;gap:5px;color:var(--ink)}
  .hotline .hours{font-size:18px;font-weight:800}
  .hotline .caption{font-size:8px;font-weight:700;font-style:italic;line-height:10px}
  .hook{position:absolute;left:11px;color:var(--white);font-weight:700;line-height:1.15;letter-spacing:.2px}
  .hook .accent{color:var(--tan-light)}
  .hook .light{font-weight:400}
  .cta{position:absolute;left:12px;top:166px;color:var(--ink)}
  .cta .offer{font-size:12.5px;font-weight:700;letter-spacing:.2px}
  .cta .offer .light{font-weight:400}
  .cta .offer .accent{color:var(--tan)}
  .cta .line{font-family:"Oswald",Arial,sans-serif;font-size:15px;font-weight:500;margin-top:1px;letter-spacing:.2px}
  .contact-strip{position:absolute;left:12px;top:216px;font-size:5.5px;font-weight:700;color:var(--white);display:flex;gap:8px}

  /* back */
  .back-broker{position:absolute;left:10px;top:17px;font-size:7.5px;font-weight:700;color:var(--white)}
  .quote-mark{position:absolute;font-family:Georgia,serif;font-size:20px;font-weight:700;color:var(--white);line-height:1}
  .testimonial{position:absolute;left:11px;top:52px;width:164px;font-size:4.6px;line-height:7.8px;color:var(--white);text-align:justify}
  .attribution{position:absolute;left:90px;top:135px;font-size:6.5px;font-weight:700;color:var(--white)}
  .attribution .accent{color:var(--tan-light)}
  .office{position:absolute;left:11px;top:142px;color:var(--white);font-size:4.6px;line-height:6.5px}
  .office .label{color:var(--tan-light);font-weight:700;font-size:5px}
  .office .addr{display:flex;gap:3px;margin-top:2px}
  .back-cta{position:absolute;left:10px;top:175px;color:var(--white)}
  .back-cta .offer{font-size:9.5px;font-weight:700}
  .back-cta .offer .light{font-weight:400}
  .back-cta .mail{font-size:5.5px;font-weight:700;margin-top:3px;display:flex;gap:3px;align-items:center}
  .back-agent{position:absolute;left:176px;top:175px;color:var(--white);text-align:right}
  .back-agent .agent{font-size:10px;font-weight:700;letter-spacing:.3px}
  .back-agent .phone{font-size:11px;font-weight:700;display:flex;gap:4px;align-items:center;justify-content:flex-end;margin-top:2px}
  .back-brand{position:absolute;left:266px;top:174px;color:var(--white);font-weight:400}
  .back-brand .name{font-size:10px;line-height:11px;display:block}
  .back-brand .sub{font-size:5.5px;display:block;margin-top:5px}
  .back-web{position:absolute;left:10px;top:217px;font-size:5.5px;font-weight:700;color:var(--white)}
  .stamp{position:absolute;left:302px;top:11px;width:53px;height:51px;border:1px solid #9a9a9a}
  .mail-line{position:absolute;left:228px;width:127px;height:1px;background:#b5b5b5}
</style>
</head>
<body>

<!-- ===== FRONT CARD TEMPLATE x4 ===== -->
<section class="card front col-front row-1">
  <div class="photo" role="img" aria-label="Photo of a two-storey home with the smiling broker couple in the foreground"></div>
  <svg class="shapes" viewBox="0 0 366 230" aria-hidden="true">
    <defs><linearGradient id="silver1" x1="0" x2="1"><stop offset="0" stop-color="#f3f3f3"/><stop offset="1" stop-color="#c9c9c9"/></linearGradient></defs>
    <polygon points="0,0 158,0 140,70 0,70" fill="#b69a63"/>
    <polygon points="160,0 264,0 252,24 154,24" fill="#4a4a4a"/>
    <polygon points="142,25 256,25 234,70 130,70" fill="url(#silver1)"/>
    <polygon points="0,72 252,72 188,156 0,156" fill="#4a4a4a"/>
    <polygon points="0,161 190,161 206,205 0,205" fill="url(#silver1)"/>
    <polygon points="0,205 206,205 209,212 0,212" fill="#3c3c3c"/>
    <polygon points="0,212 209,212 216,230 0,230" fill="#b69a63"/>
  </svg>
  <div class="brand"><span class="name">HOLT &amp;<br>PARTNERS</span><span class="sub">PROPERTY MANAGEMENT</span></div>
  <div class="broker"><span class="label">Broker</span> BRE 04417328</div>
  <div class="hotline"><span class="hours">24/7</span><span class="caption">Emergency<br>Line</span></div>
  <h2 class="hook" style="top:95px;font-size:14px">DO YOUR TENANT LEASES<br>FULLY <span class="accent">PROTECT YOU?</span></h2>
  <div class="cta"><div class="offer">CALL <span class="light">FOR A</span> <span class="accent">FREE QUOTE</span></div><div class="line">GRANT HOLT 555-014-2290</div></div>
  <div class="contact-strip"><span>◉ harborviewestatesproperty.com</span><span>✉ grant@grantholtpm.com</span></div>
</section>

<section class="card front col-front row-2">
  <div class="photo" role="img" aria-label="Photo of a two-storey home with the smiling broker couple in the foreground"></div>
  <svg class="shapes" viewBox="0 0 366 230" aria-hidden="true">
    <defs><linearGradient id="silver2" x1="0" x2="1"><stop offset="0" stop-color="#f3f3f3"/><stop offset="1" stop-color="#c9c9c9"/></linearGradient></defs>
    <polygon points="0,0 158,0 140,70 0,70" fill="#b69a63"/>
    <polygon points="160,0 264,0 252,24 154,24" fill="#4a4a4a"/>
    <polygon points="142,25 256,25 234,70 130,70" fill="url(#silver2)"/>
    <polygon points="0,72 252,72 188,156 0,156" fill="#4a4a4a"/>
    <polygon points="0,161 190,161 206,205 0,205" fill="url(#silver2)"/>
    <polygon points="0,205 206,205 209,212 0,212" fill="#3c3c3c"/>
    <polygon points="0,212 209,212 216,230 0,230" fill="#b69a63"/>
  </svg>
  <div class="brand"><span class="name">HOLT &amp;<br>PARTNERS</span><span class="sub">PROPERTY MANAGEMENT</span></div>
  <div class="broker"><span class="label">Broker</span> BRE 04417328</div>
  <div class="hotline"><span class="hours">24/7</span><span class="caption">Emergency<br>Line</span></div>
  <h2 class="hook" style="top:86px;font-size:17px;line-height:1">TIRED OF DEALING<br><span style="font-size:9.5px"><span class="light">WITH</span> TENANT PROBLEMS <span class="accent">AT 6:00</span></span><br>ON A <span class="accent">FRIDAY NIGHT?</span></h2>
  <div class="cta"><div class="offer">CALL <span class="light">FOR A</span> <span class="accent">FREE QUOTE</span></div><div class="line">GRANT HOLT 555-014-2290</div></div>
  <div class="contact-strip"><span>◉ harborviewestatesproperty.com</span><span>✉ grant@grantholtpm.com</span></div>
</section>

<section class="card front col-front row-3">
  <div class="photo" role="img" aria-label="Photo of a two-storey home with the smiling broker couple in the foreground"></div>
  <svg class="shapes" viewBox="0 0 366 230" aria-hidden="true">
    <defs><linearGradient id="silver3" x1="0" x2="1"><stop offset="0" stop-color="#f3f3f3"/><stop offset="1" stop-color="#c9c9c9"/></linearGradient></defs>
    <polygon points="0,0 158,0 140,70 0,70" fill="#b69a63"/>
    <polygon points="160,0 264,0 252,24 154,24" fill="#4a4a4a"/>
    <polygon points="142,25 256,25 234,70 130,70" fill="url(#silver3)"/>
    <polygon points="0,72 252,72 188,156 0,156" fill="#4a4a4a"/>
    <polygon points="0,161 190,161 206,205 0,205" fill="url(#silver3)"/>
    <polygon points="0,205 206,205 209,212 0,212" fill="#3c3c3c"/>
    <polygon points="0,212 209,212 216,230 0,230" fill="#b69a63"/>
  </svg>
  <div class="brand"><span class="name">HOLT &amp;<br>PARTNERS</span><span class="sub">PROPERTY MANAGEMENT</span></div>
  <div class="broker"><span class="label">Broker</span> BRE 04417328</div>
  <div class="hotline"><span class="hours">24/7</span><span class="caption">Emergency<br>Line</span></div>
  <h2 class="hook" style="top:84px;font-size:13px;line-height:1.1"><span class="accent">WOULD YOU LIKE</span> <span class="light">TO TAKE</span><br><span class="light">YOU</span> NEXT VACATION<br><span class="accent" style="font-size:21px">WORRY FREE?</span></h2>
  <div class="cta"><div class="offer">CALL <span class="light">FOR A</span> <span class="accent">FREE QUOTE</span></div><div class="line">GRANT HOLT 555-014-2290</div></div>
  <div class="contact-strip"><span>◉ harborviewestatesproperty.com</span><span>✉ grant@grantholtpm.com</span></div>
</section>

<section class="card front col-front row-4">
  <div class="photo" role="img" aria-label="Photo of a two-storey home with the smiling broker couple in the foreground"></div>
  <svg class="shapes" viewBox="0 0 366 230" aria-hidden="true">
    <defs><linearGradient id="silver4" x1="0" x2="1"><stop offset="0" stop-color="#f3f3f3"/><stop offset="1" stop-color="#c9c9c9"/></linearGradient></defs>
    <polygon points="0,0 158,0 140,70 0,70" fill="#b69a63"/>
    <polygon points="160,0 264,0 252,24 154,24" fill="#4a4a4a"/>
    <polygon points="142,25 256,25 234,70 130,70" fill="url(#silver4)"/>
    <polygon points="0,72 252,72 188,156 0,156" fill="#4a4a4a"/>
    <polygon points="0,161 190,161 206,205 0,205" fill="url(#silver4)"/>
    <polygon points="0,205 206,205 209,212 0,212" fill="#3c3c3c"/>
    <polygon points="0,212 209,212 216,230 0,230" fill="#b69a63"/>
  </svg>
  <div class="brand"><span class="name">HOLT &amp;<br>PARTNERS</span><span class="sub">PROPERTY MANAGEMENT</span></div>
  <div class="broker"><span class="label">Broker</span> BRE 04417328</div>
  <div class="hotline"><span class="hours">24/7</span><span class="caption">Emergency<br>Line</span></div>
  <h2 class="hook" style="top:86px;font-size:13px;line-height:1.25"><span class="accent">ARE YOUR</span><br><span style="font-size:17px">TENANTS PAYING</span><br><span class="light">BELOW</span> <span class="accent">MARKET RENTS?</span></h2>
  <div class="cta"><div class="offer">CALL <span class="light">FOR A</span> <span class="accent">FREE QUOTE</span></div><div class="line">GRANT HOLT 555-014-2290</div></div>
  <div class="contact-strip"><span>◉ harborviewestatesproperty.com</span><span>✉ grant@grantholtpm.com</span></div>
</section>

<!-- ===== BACK CARDS x4 ===== -->
<section class="card back col-back row-1">
  <svg class="shapes" viewBox="0 0 366 230" aria-hidden="true">
    <polygon points="0,0 186,0 209,70 180,168 0,168" fill="#b69a63"/>
    <polygon points="0,0 176,0 199,70 170,168 0,168" fill="#4a4a4a"/>
    <polygon points="0,13 112,13 106,31 0,31" fill="#b69a63"/>
    <polygon points="0,168 148,168 141,207 0,207" fill="#b69a63"/>
    <polygon points="150,168 366,168 366,211 143,211" fill="#4a4a4a"/>
    <polygon points="0,207 141,207 136,230 0,230" fill="#3c3c3c"/>
  </svg>
  <div class="back-broker">Broker BRE 04417328</div>
  <div class="quote-mark" style="left:11px;top:36px">“</div>
  <p class="testimonial">We have trusted Holt &amp; Partners with our rental homes since 2011 and have been very pleased. Calls and repairs are handled quickly and the rent always arrives on time. Grant and his team treat our property like their own, and the leases are clear and fair. We recommend them to any owner who wants less stress and steady income. It really makes life easy.</p>
  <div class="attribution">FROM <span class="accent">Marion L.</span></div>
  <div class="quote-mark" style="left:156px;top:130px">”</div>
  <div class="office"><div class="label">OFFICE ADDRESS</div><div class="addr"><svg width="5" height="7" viewBox="0 0 10 14"><path d="M5 0a5 5 0 0 0-5 5c0 4 5 9 5 9s5-5 5-9a5 5 0 0 0-5-5zm0 7a2 2 0 1 1 0-4 2 2 0 0 1 0 4z" fill="#c8ae78"/></svg><span>18 Harbor Crest Plaza, Suite 2<br>Harborview Estates, CA 90000</span></div></div>
  <div class="back-cta"><div class="offer">CALL <span class="light">FOR A</span> FREE QUOTE</div><div class="mail">✉ grant@grantholtpm.com</div></div>
  <div class="back-agent"><div class="agent">GRANT HOLT</div><div class="phone"><svg width="9" height="9" viewBox="0 0 20 20"><circle cx="10" cy="10" r="9" fill="none" stroke="#c8ae78" stroke-width="2"/><path d="M7 5l2 3-1 1c1 2 2 3 3 3l1-1 3 2-1 2c-4 0-8-4-8-8z" fill="#c8ae78"/></svg>555-014-2290</div></div>
  <div class="back-brand"><span class="name">HOLT &amp;<br>PARTNERS</span><span class="sub">PROPERTY MANAGEMENT</span></div>
  <div class="back-web">◉ harborviewestatesproperty.com</div>
  <div class="stamp"></div>
  <div class="mail-line" style="top:98px"></div><div class="mail-line" style="top:124px"></div><div class="mail-line" style="top:147px"></div>
</section>

<section class="card back col-back row-2">
  <svg class="shapes" viewBox="0 0 366 230" aria-hidden="true">
    <polygon points="0,0 186,0 209,70 180,168 0,168" fill="#b69a63"/>
    <polygon points="0,0 176,0 199,70 170,168 0,168" fill="#4a4a4a"/>
    <polygon points="0,13 112,13 106,31 0,31" fill="#b69a63"/>
    <polygon points="0,168 148,168 141,207 0,207" fill="#b69a63"/>
    <polygon points="150,168 366,168 366,211 143,211" fill="#4a4a4a"/>
    <polygon points="0,207 141,207 136,230 0,230" fill="#3c3c3c"/>
  </svg>
  <div class="back-broker">Broker BRE 04417328</div>
  <div class="quote-mark" style="left:11px;top:36px">“</div>
  <p class="testimonial">We have trusted Holt &amp; Partners with our rental homes since 2011 and have been very pleased. Calls and repairs are handled quickly and the rent always arrives on time. Grant and his team treat our property like their own, and the leases are clear and fair. We recommend them to any owner who wants less stress and steady income. It really makes life easy.</p>
  <div class="attribution">FROM <span class="accent">Marion L.</span></div>
  <div class="quote-mark" style="left:156px;top:130px">”</div>
  <div class="office"><div class="label">OFFICE ADDRESS</div><div class="addr"><svg width="5" height="7" viewBox="0 0 10 14"><path d="M5 0a5 5 0 0 0-5 5c0 4 5 9 5 9s5-5 5-9a5 5 0 0 0-5-5zm0 7a2 2 0 1 1 0-4 2 2 0 0 1 0 4z" fill="#c8ae78"/></svg><span>18 Harbor Crest Plaza, Suite 2<br>Harborview Estates, CA 90000</span></div></div>
  <div class="back-cta"><div class="offer">CALL <span class="light">FOR A</span> FREE QUOTE</div><div class="mail">✉ grant@grantholtpm.com</div></div>
  <div class="back-agent"><div class="agent">GRANT HOLT</div><div class="phone"><svg width="9" height="9" viewBox="0 0 20 20"><circle cx="10" cy="10" r="9" fill="none" stroke="#c8ae78" stroke-width="2"/><path d="M7 5l2 3-1 1c1 2 2 3 3 3l1-1 3 2-1 2c-4 0-8-4-8-8z" fill="#c8ae78"/></svg>555-014-2290</div></div>
  <div class="back-brand"><span class="name">HOLT &amp;<br>PARTNERS</span><span class="sub">PROPERTY MANAGEMENT</span></div>
  <div class="back-web">◉ harborviewestatesproperty.com</div>
  <div class="stamp"></div>
  <div class="mail-line" style="top:98px"></div><div class="mail-line" style="top:124px"></div><div class="mail-line" style="top:147px"></div>
</section>

<section class="card back col-back row-3">
  <svg class="shapes" viewBox="0 0 366 230" aria-hidden="true">
    <polygon points="0,0 186,0 209,70 180,168 0,168" fill="#b69a63"/>
    <polygon points="0,0 176,0 199,70 170,168 0,168" fill="#4a4a4a"/>
    <polygon points="0,13 112,13 106,31 0,31" fill="#b69a63"/>
    <polygon points="0,168 148,168 141,207 0,207" fill="#b69a63"/>
    <polygon points="150,168 366,168 366,211 143,211" fill="#4a4a4a"/>
    <polygon points="0,207 141,207 136,230 0,230" fill="#3c3c3c"/>
  </svg>
  <div class="back-broker">Broker BRE 04417328</div>
  <div class="quote-mark" style="left:11px;top:36px">“</div>
  <p class="testimonial">We have trusted Holt &amp; Partners with our rental homes since 2011 and have been very pleased. Calls and repairs are handled quickly and the rent always arrives on time. Grant and his team treat our property like their own, and the leases are clear and fair. We recommend them to any owner who wants less stress and steady income. It really makes life easy.</p>
  <div class="attribution">FROM <span class="accent">Marion L.</span></div>
  <div class="quote-mark" style="left:156px;top:130px">”</div>
  <div class="office"><div class="label">OFFICE ADDRESS</div><div class="addr"><svg width="5" height="7" viewBox="0 0 10 14"><path d="M5 0a5 5 0 0 0-5 5c0 4 5 9 5 9s5-5 5-9a5 5 0 0 0-5-5zm0 7a2 2 0 1 1 0-4 2 2 0 0 1 0 4z" fill="#c8ae78"/></svg><span>18 Harbor Crest Plaza, Suite 2<br>Harborview Estates, CA 90000</span></div></div>
  <div class="back-cta"><div class="offer">CALL <span class="light">FOR A</span> FREE QUOTE</div><div class="mail">✉ grant@grantholtpm.com</div></div>
  <div class="back-agent"><div class="agent">GRANT HOLT</div><div class="phone"><svg width="9" height="9" viewBox="0 0 20 20"><circle cx="10" cy="10" r="9" fill="none" stroke="#c8ae78" stroke-width="2"/><path d="M7 5l2 3-1 1c1 2 2 3 3 3l1-1 3 2-1 2c-4 0-8-4-8-8z" fill="#c8ae78"/></svg>555-014-2290</div></div>
  <div class="back-brand"><span class="name">HOLT &amp;<br>PARTNERS</span><span class="sub">PROPERTY MANAGEMENT</span></div>
  <div class="back-web">◉ harborviewestatesproperty.com</div>
  <div class="stamp"></div>
  <div class="mail-line" style="top:98px"></div><div class="mail-line" style="top:124px"></div><div class="mail-line" style="top:147px"></div>
</section>

<section class="card back col-back row-4">
  <svg class="shapes" viewBox="0 0 366 230" aria-hidden="true">
    <polygon points="0,0 186,0 209,70 180,168 0,168" fill="#b69a63"/>
    <polygon points="0,0 176,0 199,70 170,168 0,168" fill="#4a4a4a"/>
    <polygon points="0,13 112,13 106,31 0,31" fill="#b69a63"/>
    <polygon points="0,168 148,168 141,207 0,207" fill="#b69a63"/>
    <polygon points="150,168 366,168 366,211 143,211" fill="#4a4a4a"/>
    <polygon points="0,207 141,207 136,230 0,230" fill="#3c3c3c"/>
  </svg>
  <div class="back-broker">Broker BRE 04417328</div>
  <div class="quote-mark" style="left:11px;top:36px">“</div>
  <p class="testimonial">We have trusted Holt &amp; Partners with our rental homes since 2011 and have been very pleased. Calls and repairs are handled quickly and the rent always arrives on time. Grant and his team treat our property like their own, and the leases are clear and fair. We recommend them to any owner who wants less stress and steady income. It really makes life easy.</p>
  <div class="attribution">FROM <span class="accent">Marion L.</span></div>
  <div class="quote-mark" style="left:156px;top:130px">”</div>
  <div class="office"><div class="label">OFFICE ADDRESS</div><div class="addr"><svg width="5" height="7" viewBox="0 0 10 14"><path d="M5 0a5 5 0 0 0-5 5c0 4 5 9 5 9s5-5 5-9a5 5 0 0 0-5-5zm0 7a2 2 0 1 1 0-4 2 2 0 0 1 0 4z" fill="#c8ae78"/></svg><span>18 Harbor Crest Plaza, Suite 2<br>Harborview Estates, CA 90000</span></div></div>
  <div class="back-cta"><div class="offer">CALL <span class="light">FOR A</span> FREE QUOTE</div><div class="mail">✉ grant@grantholtpm.com</div></div>
  <div class="back-agent"><div class="agent">GRANT HOLT</div><div class="phone"><svg width="9" height="9" viewBox="0 0 20 20"><circle cx="10" cy="10" r="9" fill="none" stroke="#c8ae78" stroke-width="2"/><path d="M7 5l2 3-1 1c1 2 2 3 3 3l1-1 3 2-1 2c-4 0-8-4-8-8z" fill="#c8ae78"/></svg>555-014-2290</div></div>
  <div class="back-brand"><span class="name">HOLT &amp;<br>PARTNERS</span><span class="sub">PROPERTY MANAGEMENT</span></div>
  <div class="back-web">◉ harborviewestatesproperty.com</div>
  <div class="stamp"></div>
  <div class="mail-line" style="top:98px"></div><div class="mail-line" style="top:124px"></div><div class="mail-line" style="top:147px"></div>
</section>

</body>
</html>
```